Illustration / Infographic for HOMEBROKERĀ®

I'm a Canadian real estate agent who offers a 50% cashback program to Buyers on my commission.

I also offer two packages to Sellers;
-2.5% full service model
-$999 Flat Fee PLX

I need to be able to explain my CashBack incentive program, 2.5% Full Service, & $999 Flat Fee PLX in an easy to understand and read format.

I have attached my current graphic, which many people still don't understand. I need it more visually appealing / web 2.0 style.

I would like a illustration / infographic that can be use for both the 50% CashBack, 2.5%, and $999 Flat Fee.

You can learn more about my program here:
http://corvan-teller.example/sell-your-home-for-less-victoria/
http://corvan-teller.example/999-flat-fee-plx/
http://corvan-teller.example/cash-back-program/

Don't worry on the content details, just layout and design for now, and then I will provide winner with required details. I have attached my attempt to create an illustration in photoshop. Would prefer .PSD

Target Market(s)

New Home Buyers
General Public with little to no knowledge of Homebroker commissions

Industry/Entity Type

Real Estate

Font styles to use
Sans Serif

Colors
3276b5
33a6d7
faee3e
1b1b1b
eb1f27

Requirements
Must have
• Photoshop

```html
<!DOCTYPE html>
<html lang="en">
<head>
<meta charset="utf-8">
<title>Homebroker Commission Breakdown</title>
<link rel="stylesheet" href="https://fonts.googleapis.com/css2?family=Source+Sans+3:wght@400;600;700&display=swap">
<style>
  :root {
    --frame-blue: #33a6d7;
    --field-blue: #2f72ad;
    --field-blue-dark: #245f96;
    --title-blue: #3276b5;
    --accent-yellow: #faee3e;
    --pill-dark: #1b1b1b;
    --price-red: #eb1f27;
    --strike-grey: #5a5a5a;
    --ink: #1b1b1b;
    --card-white: #ffffff;
    --card-fade: #d9dadc;
    --connector: #ffffff;
  }
  * { box-sizing: border-box; margin: 0; padding: 0; }
  html, body { width: 1200px; height: 867px; overflow: hidden; }
  body {
    font-family: "Source Sans 3", "Myriad Pro", sans-serif;
    background: var(--frame-blue);
  }
  .canvas { position: relative; width: 1200px; height: 867px; }
  .field {
    position: absolute; left: 25px; top: 30px; width: 1150px; height: 809px;
    background: radial-gradient(ellipse at 50% 40%, var(--field-blue) 0%, var(--field-blue-dark) 100%);
    box-shadow: inset 0 0 30px rgba(0,0,0,.25);
  }
  .connectors { position: absolute; left: 0; top: 0; }

  .seller-card {
    position: absolute; left: 141px; top: 51px; width: 283px; height: 248px;
    background: var(--card-white); box-shadow: 0 3px 8px rgba(0,0,0,.35);
    overflow: hidden;
  }
  .seller-card .home-art {
    position: absolute; left: 6px; top: 6px; width: 271px; height: 164px;
    background: linear-gradient(#3a9ee0 0%, #bfe3f7 60%, #c9a24a 61%, #8a6a2a 85%, #2f8a3a 100%);
  }
  .seller-ribbon {
    position: absolute; left: -34px; top: 20px; width: 160px; height: 30px;
    transform: rotate(-32deg);
    background: linear-gradient(#f4f4f4, #b9b9b9);
    color: var(--ink); font-weight: 700; font-size: 21px; text-align: center; line-height: 30px;
    box-shadow: 0 2px 4px rgba(0,0,0,.4);
  }
  .sale-price { position: absolute; left: 40px; top: 182px; font-size: 22px; color: var(--ink); }
  .sale-price .old { color: var(--price-red); text-decoration: line-through; text-decoration-color: var(--ink); text-decoration-thickness: 3px; }
  .sale-price-new { position: absolute; right: 40px; top: 210px; font-size: 27px; font-weight: 600; color: var(--price-red); }

  .tier-card {
    position: absolute; text-align: center; color: var(--ink);
    background: linear-gradient(var(--card-white) 55%, var(--card-fade) 100%);
    border-radius: 4px; box-shadow: 0 3px 8px rgba(0,0,0,.35);
  }
  .tier-card .heading { color: var(--title-blue); font-size: 24px; line-height: 1.35; }
  .tier-card .heading.plain { color: var(--ink); }
  .tier-card .rule { font-size: 21px; }
  .divider { height: 1px; background: #b9b9b9; margin: 4px 32px 9px; }

  .amount-pill {
    position: absolute; height: 49px;
    background: linear-gradient(#4a4a4a 0%, var(--pill-dark) 50%, #111 100%);
    border-radius: 4px; box-shadow: 0 2px 4px rgba(0,0,0,.5);
    display: flex; align-items: center; justify-content: center; gap: 12px;
    font-size: 25px; font-weight: 700;
  }
  .amount-pill .was { color: var(--strike-grey); text-decoration: line-through; text-decoration-color: var(--pill-dark); text-decoration-thickness: 3px; }
  .amount-pill .now { color: var(--price-red); }

  .listing-top { left: 606px; top: 141px; width: 347px; height: 197px; padding-top: 8px; }
  .listing-top .amount-pill { left: 49px; top: 130px; width: 250px; }
  .buyer-split { left: 467px; top: 428px; width: 305px; height: 154px; padding-top: 14px; }
  .buyer-split .amount-pill { left: 27px; top: 86px; width: 250px; }
  .listing-split { left: 808px; top: 428px; width: 303px; height: 154px; padding-top: 14px; }
  .listing-split .amount-pill { left: 24px; top: 94px; width: 250px; height: 50px; }
  .portion { top: 663px; width: 305px; height: 176px; padding-top: 18px; }
  .portion .heading { color: var(--ink); font-size: 23px; }
  .portion .amount-pill { left: 24px; top: 86px; width: 251px; height: 53px; }
  .agent-portion { left: 305px; }
  .cash-back { left: 652px; }
</style>
</head>
<body>
<div class="canvas">
  <div class="field"></div>

  <svg class="connectors" width="1200" height="867" viewBox="0 0 1200 867" aria-hidden="true">
    <polyline points="435,273 497,273 510,308 590,308" fill="none" stroke="var(--accent-yellow)" stroke-width="9"/>
    <polygon points="588,294 608,308 588,322" fill="var(--accent-yellow)"/>
    <g fill="none" stroke="var(--connector)" stroke-width="9">
      <polyline points="804,338 804,369"/>
      <polyline points="635,404 635,369 972,369 972,404"/>
      <polyline points="619,582 619,618"/>
      <polyline points="444,645 444,618 786,618 786,645"/>
    </g>
    <g fill="var(--connector)">
      <polygon points="621,401 649,401 635,421"/>
      <polygon points="958,401 986,401 972,421"/>
      <polygon points="430,642 458,642 444,662"/>
      <polygon points="772,642 800,642 786,662"/>
    </g>
  </svg>

  <div class="seller-card">
    <div class="home-art" role="img" aria-label="Illustration of a two-storey house with a red roof"></div>
    <div class="seller-ribbon">Seller</div>
    <div class="sale-price">Sale Price: <span class="old">$600,000</span></div>
    <div class="sale-price-new">$700,000</div>
  </div>

  <div class="tier-card listing-top">
    <div class="heading">A Listing Homebroker<br>may charge</div>
    <div class="divider"></div>
    <div class="rule">6% 100,000 + 3% balance</div>
    <div class="amount-pill"><span class="was">$ 21,000</span><span class="now">$ 24,000</span></div>
  </div>

  <div class="tier-card buyer-split">
    <div class="heading">Buyer’s Homebroker</div>
    <div class="rule">3% 100,000 + 1.5% balance</div>
    <div class="amount-pill"><span class="was">$ 10,500</span><span class="now">$ 12,000</span></div>
  </div>

  <div class="tier-card listing-split">
    <div class="heading plain">Listing Homebroker</div>
    <div class="rule">3% 100,000 + 1.5% balance</div>
    <div class="amount-pill"><span class="was">$ 10,500</span><span class="now">$ 12,000</span></div>
  </div>

  <div class="tier-card portion agent-portion">
    <div class="heading">Dario’s Portion</div>
    <div class="amount-pill"><span class="was">$ 5,500</span><span class="now">$ 6,750</span></div>
  </div>

  <div class="tier-card portion cash-back">
    <div class="heading">Cash Back to You</div>
    <div class="amount-pill"><span class="was">$ 5,500</span><span class="now">$ 5,250</span></div>
  </div>
</div>
</body>
</html>
```